Belle Rive Weddings and Events

I am a small boutique wedding coordinator, stylist and bridal consultant/coach/assistant. I am based in Brisbane, Australia and my business is geared towards mid range- high end budget bridal couples.
I am after some business cards that are double sided, with the logo on one side and all other information on the other side, including the business tagline of design, create, celebrate. The look of the card needs to be clean and crisp, with white and the tones of grey of the logo.The final design needs to convey sophistication and poise. Perhaps the logo and tagline could be done in a metallic silver with the rest of the text in the shades of grey from the style guide attached below.
Title- Mira Tolvarenko - Director / Events Manager and Stylist
Address - 218 Halbrook Terrace, Wexley Vale, QLD, 4127
Phone- 07 3894 2167
Mobile- 0438 725 519
Email- Mira@bellerivecelebra.com.au
Website- www.bellerivecelebra.com.au

```html
<!DOCTYPE html>
<html lang="en">
<head>
<meta charset="utf-8">
<title>Belle Rive Weddings and Events – Business Cards</title>
<link rel="stylesheet" href="https://fonts.googleapis.com/css2?family=Montserrat:wght@700&family=Questrial&display=swap">
<style>
  :root {
    --backdrop: #e6e4e1;
    --card: #fbfbfb;
    --card-pattern: #f1f1f1;
    --silver: #a9a9a9;
    --silver-light: #c9c9c9;
    --ink: #6e6e6e;
    --ink-dark: #555555;
    --icon: #7a7a7a;
  }
  * { box-sizing: border-box; margin: 0; padding: 0; }
  html, body { width: 1200px; height: 855px; overflow: hidden; }
  body {
    background: var(--backdrop);
    font-family: "Questrial", "Century Gothic", sans-serif;
    color: var(--ink);
    position: relative;
  }
  .card {
    position: absolute;
    top: 272px;
    width: 520px;
    height: 310px;
    border-radius: 26px;
    background: var(--card);
    box-shadow: 0 6px 18px rgba(0,0,0,0.12);
    overflow: hidden;
  }
  .card-front { left: 50px; }
  .card-back { left: 630px; }

  .damask-field {
    position: absolute;
    inset: 0;
    background: radial-gradient(ellipse at 50% 50%, var(--card) 0%, var(--card-pattern) 100%);
  }

  /* Front */
  .front-band {
    position: absolute;
    top: 0; bottom: 0;
    left: 430px;
    width: 22px;
    background: var(--silver-light);
  }
  .front-website {
    position: absolute;
    left: 398px;
    top: 155px;
    transform: translate(-50%, -50%) rotate(-90deg);
    white-space: nowrap;
    font-size: 15px;
    letter-spacing: 0.5px;
    color: var(--ink);
  }
  .logo-circle {
    position: absolute;
    left: 75px;
    top: 55px;
    width: 200px;
    height: 200px;
    border-radius: 50%;
    border: 1.5px solid var(--silver);
  }
  .logo-name {
    position: absolute;
    left: 75px;
    top: 55px;
    width: 200px;
    height: 200px;
    display: flex;
    flex-direction: column;
    align-items: center;
    justify-content: center;
    color: var(--silver);
    text-align: center;
    line-height: 1.2;
  }
  .logo-name .name-main { font-size: 34px; }
  .logo-name .name-sub { font-size: 11px; letter-spacing: 1px; margin-top: 4px; }

  /* Back */
  .back-band {
    position: absolute;
    left: 0; right: 0;
    height: 22px;
    background: var(--silver-light);
  }
  .back-band.top { top: 30px; }
  .back-band.bottom { top: 200px; }
  .person {
    position: absolute;
    left: 28px;
    top: 72px;
    width: 230px;
  }
  .person-name {
    font-family: "Montserrat", "Century Gothic", sans-serif;
    font-weight: 700;
    font-size: 18px;
    letter-spacing: 0.5px;
    color: var(--ink-dark);
    text-transform: uppercase;
    white-space: nowrap;
  }
  .person-title { font-size: 11.5px; margin-top: 8px; color: var(--ink); }
  .divider {
    position: absolute;
    left: 268px;
    top: 70px;
    width: 1px;
    height: 110px;
    background: var(--silver);
  }
  .contacts {
    position: absolute;
    left: 284px;
    top: 72px;
    list-style: none;
    font-size: 13px;
    color: var(--ink);
  }
  .contacts li { display: flex; align-items: center; gap: 8px; height: 34px; white-space: nowrap; }
  .contacts svg { width: 16px; height: 16px; flex: none; }
  .address {
    position: absolute;
    left: 28px;
    top: 248px;
    font-size: 14px;
    color: var(--ink);
    white-space: nowrap;
  }
</style>
</head>
<body>
  <section class="card card-front" aria-label="Business card front">
    <div class="damask-field" role="img" aria-label="Soft grey damask pattern background"></div>
    <div class="logo-circle"></div>
    <div class="logo-name">
      <span class="name-main">Belle Rive</span>
      <span class="name-sub">Weddings and Events</span>
    </div>
    <p class="front-website">www.bellerivecelebra.com.au</p>
    <div class="front-band" role="img" aria-label="Silver lace ribbon band"></div>
  </section>

  <section class="card card-back" aria-label="Business card back">
    <div class="damask-field" role="img" aria-label="Soft grey damask pattern background"></div>
    <div class="back-band top" role="img" aria-label="Silver lace ribbon band"></div>
    <div class="person">
      <h1 class="person-name">Mira Tolvarenko</h1>
      <p class="person-title">Director / Events Manager and Stylist</p>
    </div>
    <div class="divider"></div>
    <ul class="contacts">
      <li>
        <svg viewBox="0 0 16 16" aria-hidden="true"><circle cx="8" cy="8" r="8" fill="var(--icon)"/><path d="M5.2 4.5l1.6-.3.8 1.8-1 .7c.4 1 1 1.7 2 2.2l.7-1 1.8.8-.3 1.6c-3.2.2-5.8-2.4-5.6-5.8z" fill="#fff"/></svg>
        07 3894 2167
      </li>
      <li>
        <svg viewBox="0 0 16 16" aria-hidden="true"><circle cx="8" cy="8" r="8" fill="var(--icon)"/><rect x="5.5" y="3.5" width="5" height="9" rx="1" fill="#fff"/><rect x="6.3" y="4.6" width="3.4" height="5.6" fill="var(--icon)"/></svg>
        0438 725 519
      </li>
      <li>
        <svg viewBox="0 0 16 16" aria-hidden="true"><circle cx="8" cy="8" r="8" fill="var(--icon)"/><rect x="4" y="5" width="8" height="6" fill="#fff"/><path d="M4 5l4 3.3L12 5" fill="none" stroke="var(--icon)" stroke-width="0.9"/></svg>
        Mira@bellerivecelebra.com.au
      </li>
    </ul>
    <div class="back-band bottom" role="img" aria-label="Silver lace ribbon band"></div>
    <p class="address">218 Halbrook Terrace, Wexley Vale, QLD, 4127</p>
  </section>
</body>
</html>
```